BrindleWorks Business Card Design

Design business cards with attached ideas. I am open to several different ideas that would be interesting and innovative. What I have provided is logo and colors. Font should be Helvetica although it could be bold or light as needed. The design can be vertical or horizontal. The design should be more interesting than a standard business card. Files must be ready to send to a printer and in Illustrator format. The text with the five icons should be exact. Send me some ideas and I will get back to you right away. I need to choose a design within 3-5 days.

Target Market(s)

Business audience

Industry/Entity Type

Business

Contact Information for Business Card

Files should be ready to send to printer in illustrator format

Font styles to use
Sans Serif

Colors
3276b5

Requirements
Must have
• Use attached logo and two colors - blue / gray
• Include 5 offering icons and text on back
Nice to have
• Interesting and innovative design. Vertical or horizontal are both fine.

```html
<!DOCTYPE html>
<html lang="en">
<head>
<meta charset="utf-8">
<title>BrindleWorks Business Card</title>
<link href="https://fonts.googleapis.com/css2?family=Arimo:wght@400;700&display=swap" rel="stylesheet">
<style>
  :root {
    --brand-blue: #3276b5;
    --band-edge: #8fb3d6;
    --card-gray: #5b5c5e;
    --ink: #2f2f31;
    --white: #ffffff;
    --stage: #e9eaec;
    --line-soft: rgba(255,255,255,0.55);
  }
  * { box-sizing: border-box; margin: 0; padding: 0; }
  html, body { width: 1200px; height: 900px; overflow: hidden; }
  body {
    background: var(--stage);
    font-family: "Arimo", Helvetica, Arial, sans-serif;
    position: relative;
  }
  .card {
    position: absolute;
    left: 280px;
    width: 640px;
    height: 366px;
    border-radius: 4px;
    overflow: hidden;
    box-shadow: 0 8px 24px rgba(0,0,0,0.18);
  }

  /* Back side */
  .card-back { top: 64px; background: var(--card-gray); color: var(--white); }
  .back-brand {
    position: absolute; top: 26px; left: 0; right: 0;
    display: flex; justify-content: center; align-items: center; gap: 14px;
  }
  .brand-square { width: 40px; height: 40px; background: var(--white); border-radius: 3px; flex: 0 0 auto; }
  .brand-text { display: flex; flex-direction: column; }
  .brand-name { font-weight: 700; font-size: 30px; letter-spacing: -0.5px; line-height: 1; }
  .brand-tagline { font-size: 11px; margin-top: 4px; }
  .offerings {
    position: absolute; left: 110px; right: 110px; top: 96px; bottom: 26px;
    border: 1px solid var(--line-soft);
    padding: 16px 22px 0;
  }
  .offerings-title {
    text-align: center; font-size: 17px; font-weight: 400; letter-spacing: 0.5px;
    text-transform: uppercase; margin-bottom: 14px;
  }
  .offering-list { list-style: none; }
  .offering {
    display: flex; align-items: center; gap: 10px;
    font-size: 15px; margin-bottom: 13px; white-space: nowrap;
  }
  .offering strong { font-weight: 700; }
  .offering-icon {
    width: 22px; height: 22px; flex: 0 0 22px;
    background: var(--white); border-radius: 50%;
    display: flex; align-items: center; justify-content: center;
  }

  /* Front side */
  .card-front { top: 470px; background: var(--white); }
  .front-band {
    position: absolute; left: 0; right: 0; bottom: 0; height: 138px;
    background: var(--brand-blue);
    border-top: 4px solid var(--band-edge);
  }
  .front-panel {
    position: absolute; right: 0; top: 118px; width: 250px; bottom: 0;
    background: var(--brand-blue);
    border-top: 4px solid var(--band-edge);
  }
  .front-brand {
    position: absolute; top: 46px; left: 110px;
    display: flex; align-items: center; gap: 14px;
  }
  .front-brand .brand-square { width: 58px; height: 58px; background: var(--brand-blue); }
  .front-brand .brand-name { color: var(--brand-blue); font-size: 40px; }
  .front-brand .brand-tagline { color: var(--ink); font-size: 13px; font-weight: 700; }
  .divider {
    position: absolute; left: 372px; top: 190px; width: 1px; height: 110px;
    background: var(--white); z-index: 2;
  }
  .holder {
    position: absolute; right: 30px; top: 150px; width: 210px;
    color: var(--white); z-index: 2; text-align: right;
  }
  .holder-name { font-weight: 700; font-size: 22px; }
  .holder-role { font-size: 15px; margin-top: 6px; }
  .contact {
    position: absolute; left: 92px; bottom: 26px; list-style: none;
    color: var(--white); z-index: 2;
  }
  .contact li { display: flex; align-items: center; gap: 8px; font-size: 16px; margin-top: 8px; }
  .contact svg { width: 14px; height: 14px; }
</style>
</head>
<body>

<section class="card card-back" aria-label="Card back">
  <div class="back-brand">
    <div class="brand-square"></div>
    <div class="brand-text">
      <span class="brand-name">BrindleWorks</span>
      <span class="brand-tagline">Sharper Plans - Stronger Teams</span>
    </div>
  </div>
  <div class="offerings">
    <h2 class="offerings-title">BrindleWorks Offerings</h2>
    <ul class="offering-list">
      <li class="offering">
        <span class="offering-icon"><svg width="12" height="12" viewBox="0 0 12 12"><rect x="2" y="1" width="8" height="10" fill="#3276b5"/><rect x="4" y="3" width="4" height="1" fill="#fff"/></svg></span>
        <span><strong>Concepts:</strong> Thought leadership white papers</span>
      </li>
      <li class="offering">
        <span class="offering-icon"><svg width="12" height="12" viewBox="0 0 12 12"><circle cx="6" cy="4" r="2.5" fill="#3276b5"/><path d="M1.5 11 a4.5 4 0 0 1 9 0z" fill="#3276b5"/></svg></span>
        <span><strong>Curriculum:</strong> Short courses on strategy</span>
      </li>
      <li class="offering">
        <span class="offering-icon"><svg width="12" height="12" viewBox="0 0 12 12"><rect x="1" y="3" width="2" height="6" fill="#3276b5"/><rect x="9" y="3" width="2" height="6" fill="#3276b5"/><rect x="3" y="5.3" width="6" height="1.4" fill="#3276b5"/></svg></span>
        <span><strong>Coaching:</strong> Building your strategic leadership</span>
      </li>
      <li class="offering">
        <span class="offering-icon"><svg width="12" height="12" viewBox="0 0 12 12"><circle cx="6" cy="2.5" r="1.8" fill="#3276b5"/><circle cx="2.5" cy="9" r="1.8" fill="#3276b5"/><circle cx="9.5" cy="9" r="1.8" fill="#3276b5"/><path d="M6 2.5 L2.5 9 M6 2.5 L9.5 9" stroke="#3276b5" stroke-width="1"/></svg></span>
        <span><strong>Consulting:</strong> Developing your strategic future</span>
      </li>
      <li class="offering">
        <span class="offering-icon"><svg width="12" height="12" viewBox="0 0 12 12"><rect x="1" y="2" width="10" height="8" fill="#3276b5"/><path d="M3 5h6M3 7h4" stroke="#fff" stroke-width="1"/></svg></span>
        <span><strong>ScoreCard:</strong> Balanced ScoreCard and software</span>
      </li>
    </ul>
  </div>
</section>

<section class="card card-front" aria-label="Card front">
  <div class="front-band"></div>
  <div class="front-panel"></div>
  <div class="front-brand">
    <div class="brand-square"></div>
    <div class="brand-text">
      <span class="brand-name">BrindleWorks</span>
      <span class="brand-tagline">Sharper Plans - Stronger Teams</span>
    </div>
  </div>
  <div class="divider"></div>
  <div class="holder">
    <p class="holder-name">Dana Kessler, PhD</p>
    <p class="holder-role">Managing Director</p>
  </div>
  <ul class="contact">
    <li><svg viewBox="0 0 14 14"><path d="M2 4 Q7 0 12 4 L10 6 L8 5 L6 5 L4 6z M3 8h8v4H3z" fill="#fff"/></svg>: 555-014-2270</li>
    <li><svg viewBox="0 0 14 14"><circle cx="7" cy="7" r="6" fill="#fff"/><path d="M4 5 Q7 7 6 10 M9 3 Q8 6 11 8" stroke="#3276b5" stroke-width="1.2" fill="none"/></svg>: BrindleWorks.com</li>
    <li><svg viewBox="0 0 14 14"><rect x="1" y="3" width="12" height="8" fill="#fff"/><path d="M1 3 L7 8 L13 3" stroke="#3276b5" stroke-width="1" fill="none"/></svg>: dana@BrindleWorks.com</li>
  </ul>
</section>

</body>
</html>
```